Business card on Pvc transparent frosted

I need a business advertising card that will be eye catching and fun.
Target Market(s)
Rednecks, country, hunters, Fisherman, ATV users, lifted trucks, cowboys, cattle ranchers, farmers, etc
Industry/Entity Type
Apparel Store
Contact Information for Business Card
This will he printed on single side of a transparent frosted plastic card with shinny foil print option.
Requirements
Must have
- 1 - My logo.
- 2 - HOLLER BOOTSTRAP OUTFITTERS
- 3 - my motto "DONT judge how we look..... Judge the WILD mess we make!!"; 4 - my website "hollerbootstrap@mailvex.example"

Nice to have
- Use your imagination with negative space, partial graffics, etc. Keep in mind you can kind of see through the card

Should not have
- Do not change colors of chevrons

```html
<!DOCTYPE html>
<html lang="en">
<head>
<meta charset="utf-8">
<title>Holler Bootstrap Outfitters – Business Card</title>
<link rel="stylesheet" href="https://fonts.googleapis.com/css2?family=Source+Sans+3:wght@400;700&display=swap">
<style>
  :root {
    --backdrop: #ecebe8;
    --card: #ffffff;
    --red: #ee2128;
    --yellow: #f8d13c;
    --ink: #1e1e1e;
  }
  * { box-sizing: border-box; margin: 0; padding: 0; }
  html, body {
    width: 1200px;
    height: 902px;
    overflow: hidden;
    background: var(--backdrop);
    font-family: "Source Sans 3", "Myriad Pro", Arial, sans-serif;
  }
  .card {
    position: absolute;
    left: 100px;
    top: 165px;
    width: 1000px;
    height: 572px;
    background: var(--card);
    border: 3px solid var(--red);
    overflow: hidden;
  }
  .card__shapes {
    position: absolute;
    inset: 0;
    width: 100%;
    height: 100%;
  }
  .brand-mark {
    position: absolute;
    left: 70px;
    top: 175px;
    display: flex;
    align-items: center;
    gap: 12px;
  }
  .brand-mark__square {
    width: 26px;
    height: 26px;
    background: var(--red);
  }
  .brand-mark__name {
    font-weight: 700;
    font-size: 30px;
    color: var(--red);
    letter-spacing: 0.5px;
  }
  .contact {
    position: absolute;
    right: 40px;
    top: 330px;
    text-align: left;
  }
  .contact__company {
    font-weight: 700;
    font-size: 30px;
    color: var(--ink);
    letter-spacing: -0.3px;
    margin-bottom: 10px;
  }
  .contact__email {
    display: flex;
    align-items: center;
    gap: 12px;
    font-size: 26px;
    color: var(--ink);
  }
  .contact__icon { width: 24px; height: 24px; flex: none; }
  .motto {
    position: absolute;
    left: 40px;
    bottom: 34px;
    font-size: 31px;
    color: var(--red);
    white-space: nowrap;
  }
</style>
</head>
<body>
  <section class="card" aria-label="Holler Bootstrap Outfitters business card">
    <svg class="card__shapes" viewBox="0 0 1000 572" preserveAspectRatio="none" aria-hidden="true">
      <path class="swoosh-yellow" d="M700 0 L1000 0 L1000 465 L430 465 C560 330 660 170 700 0 Z" fill="var(--yellow)"/>
      <path class="swoosh-red" d="M615 0 L700 0 C660 170 560 330 430 465 L385 465 C500 330 585 170 615 0 Z" fill="var(--red)"/>
      <path class="swoosh-red-tip" d="M700 0 L770 0 L706 22 Z" fill="var(--red)"/>
    </svg>

    <div class="brand-mark">
      <span class="brand-mark__square"></span>
      <span class="brand-mark__name">HOLLER BOOTSTRAP</span>
    </div>

    <div class="contact">
      <p class="contact__company">HOLLER BOOTSTRAP OUTFITTERS</p>
      <p class="contact__email">
        <svg class="contact__icon" viewBox="0 0 24 24" aria-hidden="true">
          <path d="M2 10 L12 3 L22 10 L22 21 L2 21 Z" fill="var(--ink)"/>
          <path d="M2 10 L12 16 L22 10" fill="none" stroke="var(--yellow)" stroke-width="1.6"/>
        </svg>
        hollerbootstrap@mailvex.example
      </p>
    </div>

    <p class="motto">my motto "DONT judge how we look..... Judge the WILD mess we make!!";</p>
  </section>
</body>
</html>
```